Redesign popular non profit computer donation and recycling website

We wish to make our website more high tech, more modern and feature all of our wonderful stories and offerings in easy to navigate location

Design will need to implement some dynamic variables, such as lists of charities, depot locations, and current content management system, folio grove pro

We wish to feature all of ojr media videos on the front page as well as the most recent donations

we wish to highlight our service offerings, hard drive shredding, volunteer to earn programs, computer store, etc

many of these great things are hard to find on the current layout

There is 2 designs that really catch our attention and we want to improve on both of those

Can we make the bottom blue?

How will the images that are in circles be rotated?

Can we make the latest donations section , 2/3 how it is of the page, and 1/3 make a section for Media, which will include all of our media highlights (vidlorn videos)

We really would like to feature our vidlorn videos on the front page

Can we add a live blurbix feed to the website.

Can we see how you will implement the depot locations inside of this design?
Can we see how you will implement the computer store with this design?
Currently located to www.umk.ca / login / wholesale / computer store shopping cart link

Can we see how you will change the contact us page
Can we see how you plan to display the list of waiting charities
Can we see how you plan to display all of our news feature articles 
Can we see how you plan to display our data destruction page

As we near the end of the contest I'd like to ask the designers the following;

The website must use h1,h2,h3,h4 in hierarchy only.. not starting with h6 or something random.. heading tags must only be used for actual headings.. html5 required, jquery installed and all elements of the design programmed in jquery only.. make sure lists are used in html whenever realistic.. no inline styles.... no classes added to paragraph, heading, or list elements allowed.

Target Market(s)

corporate donors
individuals
charities and non profits
low income people who wish to volunteer and earn a computer or laptop

Industry/Entity Type

Recycling

Requirements
Must have
• current umk logo
• high tech servers, laptops, velto switches, etc
• hard drive shredder in action
• all media stories and videos featured
• all latest donations scrolling
Nice to have
• corporate donors
• individuals
• charities and non profits
• low income people who wish to volunteer and earn a computer or laptop

```html
<!DOCTYPE html>
<html lang="en">
<head>
<meta charset="utf-8">
<title>Contact Us | umk.ca</title>
<link rel="stylesheet" href="https://fonts.googleapis.com/css2?family=Open+Sans:wght@400;600;700&family=Oswald:wght@300;400;500;600&display=swap">
<style>
:root{
  --green:#3f9b22;
  --green-dark:#2a7912;
  --green-light:#5cb83a;
  --red:#d3302b;
  --text:#6a6a6a;
  --text-dark:#3d3d3d;
  --rule:#e3e3e3;
  --blue:#2f66bf;
  --blue-line:#5a86cf;
  --sky:#5ec3ea;
  --white:#ffffff;
}
*{box-sizing:border-box;margin:0;padding:0}
html,body{width:1200px;height:3064px;overflow:hidden;background:var(--white)}
body{position:relative;font-family:"Open Sans",Arial,sans-serif;color:var(--text)}
ul{list-style:none}
a{text-decoration:none;color:inherit}

/* header */
.site-header{position:absolute;left:0;top:0;width:1200px;height:102px;border-bottom:1px solid #d8d8d8}
.brand{position:absolute;left:150px;top:12px;display:flex;flex-direction:column;align-items:flex-start;gap:4px}
.brand-row{display:flex;align-items:center;gap:8px}
.brand-dot{width:56px;height:56px;border-radius:50%;background:var(--green)}
.brand-name{font-family:"Open Sans",sans-serif;font-weight:700;font-size:22px;color:var(--green)}
.brand-tag{font-size:9px;color:var(--green);letter-spacing:.3px}
.utility-links{position:absolute;left:862px;top:10px;display:flex;gap:8px;font-size:12px;color:#555}
.utility-links li+li::before{content:"|";margin-right:8px;color:#aaa}
.main-nav{position:absolute;left:598px;top:50px;display:flex;font-size:13.5px;color:#333;text-transform:uppercase}
.main-nav li{margin-right:48px}
.main-nav li:last-child{margin-right:0}

.section-nav{position:absolute;left:0;top:102px;width:1200px;height:51px;background:linear-gradient(#55ad33,var(--green) 55%,var(--green-dark));border-top:2px solid #7cc85a}
.section-nav ul{position:absolute;left:130px;top:15px;display:flex;font-size:13px;color:var(--white);text-transform:uppercase}
.section-nav li{margin-right:27px}
.section-nav li.current{border-bottom:1px solid var(--white)}

/* contact page */
.page-title{position:absolute;left:130px;top:168px;font-family:"Oswald",sans-serif;font-weight:400;font-size:30px;color:var(--text-dark)}
.title-rule{position:absolute;left:130px;top:216px;width:60px;height:2px;background:var(--green)}
.depot-grid{position:absolute;left:130px;top:234px;width:942px;display:grid;grid-template-columns:470px 472px;grid-template-rows:413px 411px 396px 393px 396px 396px;border-top:1px solid var(--rule)}
.depot{padding-top:14px;border-bottom:1px solid var(--rule)}
.depot:nth-child(odd){padding-left:3px;border-right:1px solid var(--rule)}
.depot:nth-child(even){padding-left:38px}
.depot:nth-child(n+11){border-bottom:none}
.depot-photo{display:block;width:429px;height:194px}
.city{margin-top:20px;font-family:"Oswald",sans-serif;font-weight:500;font-size:19px;color:var(--green);text-transform:uppercase}
.depot-info{display:flex;margin-top:6px;font-size:12.5px;line-height:20px}
.depot-info ul{width:222px}
.depot-info ul+ul{width:200px}
.depot-info li{display:flex;gap:8px;margin-bottom:14px}
.depot-info ul+ul li{margin-bottom:3px}
.depot-info svg{flex:none;width:13px;height:13px;margin-top:4px;fill:#9a9a9a}
.map-link{font-weight:700;color:var(--red);text-transform:uppercase;font-size:12px}
.map-link svg{fill:var(--red)}

/* footer */
.site-footer{position:absolute;left:0;top:2645px;width:1200px;height:375px;background:var(--blue);color:var(--white)}
.newsletter{position:absolute;left:258px;top:25px;display:flex;align-items:center}
.newsletter svg{width:34px;height:28px;fill:var(--white)}
.newsletter-label{margin-left:6px;font-family:"Oswald",sans-serif;font-weight:300;font-size:21px;line-height:22px;width:140px}
.newsletter-input{margin-left:2px;width:335px;height:43px;background:var(--white);color:#888;font-size:14px;padding:12px 14px}
.newsletter-button{margin-left:15px;width:156px;height:43px;background:var(--sky);font-weight:700;font-size:15px;text-align:center;line-height:43px;text-transform:uppercase}
.footer-rule{position:absolute;left:130px;top:100px;width:942px;height:1px;background:var(--blue-line)}
.footer-col{position:absolute;top:132px}
.footer-col h2{font-family:"Oswald",sans-serif;font-weight:400;font-size:16px;margin-bottom:10px}
.quick-links{left:130px}
.quick-links .lists{display:flex;gap:0}
.quick-links ul{width:200px;font-size:13px;line-height:18px}
.payments{left:582px}
.payment-cards{display:grid;grid-template-columns:60px 60px;gap:8px 8px}
.card{height:34px;border-radius:3px;background:var(--white);color:var(--blue);font-size:11px;font-weight:700;display:flex;align-items:center;justify-content:center}
.connect{left:817px}
.social{display:flex;gap:6px;margin-bottom:14px}
.social li{width:30px;height:30px;border-radius:50%;background:var(--white)}
.contact-info h3{font-family:"Oswald",sans-serif;font-weight:400;font-size:16px;margin-bottom:8px}
.contact-info p{font-size:13px;line-height:16px}
.contact-info .city-line{font-weight:600}
.contact-info .big-phone{font-family:"Oswald",sans-serif;font-size:22px;margin-top:12px}
.footer-divider{position:absolute;left:1039px;top:222px;width:1px;height:130px;background:var(--blue-line)}
.legal{position:absolute;left:0;top:3020px;width:1200px;height:44px;background:#f4f4f4;border-top:1px solid #ddd}
.legal p{position:absolute;left:130px;top:12px;font-size:12px;color:#777}
.regions{position:absolute;left:888px;top:12px;display:flex;gap:6px}
.regions li{width:30px;height:18px}
.sr-icons{position:absolute;width:0;height:0;overflow:hidden}
</style>
</head>
<body>
<svg class="sr-icons" aria-hidden="true">
  <symbol id="i-pin" viewBox="0 0 12 12"><path d="M6 0a4 4 0 0 0-4 4c0 3 4 8 4 8s4-5 4-8a4 4 0 0 0-4-4zm0 5.6A1.6 1.6 0 1 1 6 2.4a1.6 1.6 0 0 1 0 3.2z"/></symbol>
  <symbol id="i-clock" viewBox="0 0 12 12"><path d="M6 0a6 6 0 1 0 0 12A6 6 0 0 0 6 0zm0 10.6a4.6 4.6 0 1 1 0-9.2 4.6 4.6 0 0 1 0 9.2zM6.6 2.5H5.4v4l3 1.8.6-1-2.4-1.4z"/></symbol>
  <symbol id="i-phone" viewBox="0 0 12 12"><path d="M2.4 0 4.2 2.6 3.2 4c.6 1.6 2.2 3.2 3.8 3.8l1.4-1L11 8.6 9.6 11C5 11 1 7 1 2.4z"/></symbol>
  <symbol id="i-mail" viewBox="0 0 12 12"><path d="M0 2h12v8H0zm1 1v.4l5 3.2 5-3.2V3zm0 1.6V9h10V4.6L6 7.8z"/></symbol>
  <symbol id="i-map" viewBox="0 0 12 12"><path d="M0 2 4 0l4 2 4-2v10l-4 2-4-2-4 2zm4-.6v8.4l4 2V3.4z"/></symbol>
</svg>

<header class="site-header">
  <a class="brand" href="#">
    <span class="brand-row"><span class="brand-dot"></span><span class="brand-name">umk.ca</span></span>
    <span class="brand-tag">unified material keepers</span>
  </a>
  <ul class="utility-links"><li>Login</li><li>Live Help</li><li>Live Support</li></ul>
  <ul class="main-nav"><li>Home</li><li>Pickup</li><li>Donate</li><li>Recycle</li><li>Charities</li></ul>
</header>

<nav class="section-nav">
  <ul>
    <li>About Us</li><li>Drop Off Items</li><li>Depots</li><li>Jobs</li><li>Volunteer</li><li>Pictures &amp; Videos</li><li>Links</li><li>Memberships</li><li>News</li><li class="current">Contact</li>
  </ul>
</nav>

<main>
  <h1 class="page-title">Contact Us</h1>
  <div class="title-rule"></div>

  <div class="depot-grid">
    <article class="depot">
      <svg class="depot-photo" role="img" aria-label="Calgary skyline lit up at night"><defs><linearGradient id="g1" x1="0" y1="0" x2="0" y2="1"><stop offset="0" stop-color="#3a2c2a"/><stop offset=".6" stop-color="#8a4a24"/><stop offset="1" stop-color="#c46a2c"/></linearGradient></defs><rect width="429" height="194" fill="url(#g1)"/></svg>
      <h2 class="city">Calgary</h2>
      <div class="depot-info">
        <ul>
          <li><svg><use href="#i-pin"/></svg><span>1300 52nd Avenue SE<br>Calgary, Alberta, Canada<br>T2X 4K5</span></li>
          <li><svg><use href="#i-clock"/></svg><span>Monday - Friday<br>( 9am - 5pm )</span></li>
        </ul>
        <ul>
          <li><svg><use href="#i-phone"/></svg><span>403.555.0148</span></li>
          <li><svg><use href="#i-phone"/></svg><span>1.877.5.GREENS (Toll Free)</span></li>
          <li><svg><use href="#i-mail"/></svg><span>calgary@umk.ca</span></li>
          <li class="map-link"><svg><use href="#i-map"/></svg><span>Map to Warehouse</span></li>
        </ul>
      </div>
    </article>

    <article class="depot">
      <svg class="depot-photo" role="img" aria-label="Edmonton downtown towers at night"><defs><linearGradient id="g2" x1="0" y1="0" x2="0" y2="1"><stop offset="0" stop-color="#0f1a33"/><stop offset=".55" stop-color="#3b3a3e"/><stop offset="1" stop-color="#b07a2a"/></linearGradient></defs><rect width="429" height="194" fill="url(#g2)"/></svg>
      <h2 class="city">Edmonton</h2>
      <div class="depot-info">
        <ul>
          <li><svg><use href="#i-pin"/></svg><span>6620 97th Street<br>Edmonton, Alberta, Canada<br>T5Y 2R8</span></li>
          <li><svg><use href="#i-clock"/></svg><span>Monday - Friday<br>( 9am - 5pm )</span></li>
        </ul>
        <ul>
          <li><svg><use href="#i-phone"/></svg><span>780.555.0176</span></li>
          <li><svg><use href="#i-phone"/></svg><span>1.877.5.GREENS (Toll Free)</span></li>
          <li><svg><use href="#i-mail"/></svg><span>edmonton@umk.ca</span></li>
          <li class="map-link"><svg><use href="#i-map"/></svg><span>Map to Warehouse</span></li>
        </ul>
      </div>
    </article>

    <article class="depot">
      <svg class="depot-photo" role="img" aria-label="Vancouver beach and towers by day"><defs><linearGradient id="g3" x1="0" y1="0" x2="0" y2="1"><stop offset="0" stop-color="#7fb0dc"/><stop offset=".5" stop-color="#8aa6a8"/><stop offset="1" stop-color="#b5aa8a"/></linearGradient></defs><rect width="429" height="194" fill="url(#g3)"/></svg>
      <h2 class="city">Vancouver</h2>
      <div class="depot-info">
        <ul>
          <li><svg><use href="#i-pin"/></svg><span>Call to arrange pickup<br>Vancouver, British Columbia,<br>Canada</span></li>
          <li><svg><use href="#i-clock"/></svg><span>Monday - Friday<br>( 9am - 5pm )</span></li>
        </ul>
        <ul>
          <li><svg><use href="#i-phone"/></svg><span>604.555.0132</span></li>
          <li><svg><use href="#i-phone"/></svg><span>1.877.5.GREENS (Toll Free)</span></li>
          <li><svg><use href="#i-mail"/></svg><span>vancouver@umk.ca</span></li>
          <li class="map-link"><svg><use href="#i-map"/></svg><span>Map to Warehouse</span></li>
        </ul>
      </div>
    </article>

    <article class="depot">
      <svg class="depot-photo" role="img" aria-label="Victoria parliament building lit at night"><defs><linearGradient id="g4" x1="0" y1="0" x2="0" y2="1"><stop offset="0" stop-color="#141414"/><stop offset=".5" stop-color="#6a4a14"/><stop offset="1" stop-color="#1e1a10"/></linearGradient></defs><rect width="429" height="194" fill="url(#g4)"/></svg>
      <h2 class="city">Victoria</h2>
      <div class="depot-info">
        <ul>
          <li><svg><use href="#i-pin"/></svg><span>Victoria, British Columbia,<br>Canada</span></li>
          <li><svg><use href="#i-clock"/></svg><span>Monday - Friday<br>( 9am - 5pm )</span></li>
        </ul>
        <ul>
          <li><svg><use href="#i-phone"/></svg><span>250.555.0190</span></li>
          <li><svg><use href="#i-phone"/></svg><span>1.877.5.GREENS (Toll Free)</span></li>
          <li><svg><use href="#i-mail"/></svg><span>victoria@umk.ca</span></li>
          <li class="map-link"><svg><use href="#i-map"/></svg><span>Map to Warehouse</span></li>
        </ul>
      </div>
    </article>

    <article class="depot">
      <svg class="depot-photo" role="img" aria-label="Saskatoon river and skyline at night"><defs><linearGradient id="g5" x1="0" y1="0" x2="0" y2="1"><stop offset="0" stop-color="#161c38"/><stop offset=".55" stop-color="#6a5424"/><stop offset="1" stop-color="#2a2418"/></linearGradient></defs><rect width="429" height="194" fill="url(#g5)"/></svg>
      <h2 class="city">Saskatoon</h2>
      <div class="depot-info">
        <ul>
          <li><svg><use href="#i-pin"/></svg><span>Saskatoon, Saskatchewan,<br>Canada</span></li>
          <li><svg><use href="#i-clock"/></svg><span>Monday - Friday<br>( 9am - 5pm )</span></li>
        </ul>
        <ul>
          <li><svg><use href="#i-phone"/></svg><span>1.877.5.GREENS (Toll Free)</span></li>
          <li><svg><use href="#i-mail"/></svg><span>saskatoon@umk.ca</span></li>
          <li class="map-link"><svg><use href="#i-map"/></svg><span>Map to Warehouse</span></li>
        </ul>
      </div>
    </article>

    <article class="depot">
      <svg class="depot-photo" role="img" aria-label="Winnipeg street with city lights at dusk"><defs><linearGradient id="g6" x1="0" y1="0" x2="0" y2="1"><stop offset="0" stop-color="#2a4a8a"/><stop offset=".55" stop-color="#5a3a46"/><stop offset="1" stop-color="#a0421e"/></linearGradient></defs><rect width="429" height="194" fill="url(#g6)"/></svg>
      <h2 class="city">Winnipeg</h2>
      <div class="depot-info">
        <ul>
          <li><svg><use href="#i-pin"/></svg><span>Saskatoon, Saskatchewan,<br>Canada</span></li>
          <li><svg><use href="#i-clock"/></svg><span>Monday - Friday<br>( 9am - 5pm )</span></li>
        </ul>
        <ul>
          <li><svg><use href="#i-phone"/></svg><span>1.877.5.GREENS (Toll Free)</span></li>
          <li><svg><use href="#i-mail"/></svg><span>winnipeg@umk.ca</span></li>
          <li class="map-link"><svg><use href="#i-map"/></svg><span>Map to Warehouse</span></li>
        </ul>
      </div>
    </article>

    <article class="depot">
      <svg class="depot-photo" role="img" aria-label="Montreal skyline reflected on the river at dusk"><defs><linearGradient id="g7" x1="0" y1="0" x2="0" y2="1"><stop offset="0" stop-color="#2a3c6a"/><stop offset=".55" stop-color="#5a4a44"/><stop offset="1" stop-color="#c4742a"/></linearGradient></defs><rect width="429" height="194" fill="url(#g7)"/></svg>
      <h2 class="city">Montreal</h2>
      <div class="depot-info">
        <ul>
          <li><svg><use href="#i-pin"/></svg><span>Montreal, Quebec,<br>Canada</span></li>
          <li><svg><use href="#i-clock"/></svg><span>Monday - Friday<br>( 9am - 5pm )</span></li>
        </ul>
        <ul>
          <li><svg><use href="#i-phone"/></svg><span>1.877.5.GREENS (Toll Free)</span></li>
          <li><svg><use href="#i-mail"/></svg><span>montreal@umk.ca</span></li>
          <li class="map-link"><svg><use href="#i-map"/></svg><span>Map to Warehouse</span></li>
        </ul>
      </div>
    </article>

    <article class="depot">
      <svg class="depot-photo" role="img" aria-label="Toronto waterfront skyline at night"><defs><linearGradient id="g8" x1="0" y1="0" x2="0" y2="1"><stop offset="0" stop-color="#1c2a6a"/><stop offset=".6" stop-color="#2a3a7a"/><stop offset="1" stop-color="#3a2a4a"/></linearGradient></defs><rect width="429" height="194" fill="url(#g8)"/></svg>
      <h2 class="city">Toronto</h2>
      <div class="depot-info">
        <ul>
          <li><svg><use href="#i-pin"/></svg><span>Toronto, Ontario,<br>Canada</span></li>
          <li><svg><use href="#i-clock"/></svg><span>Monday - Friday<br>( 9am - 5pm )</span></li>
        </ul>
        <ul>
          <li><svg><use href="#i-phone"/></svg><span>1.877.5.GREENS (Toll Free)</span></li>
          <li><svg><use href="#i-mail"/></svg><span>toronto@umk.ca</span></li>
          <li class="map-link"><svg><use href="#i-map"/></svg><span>Map to Warehouse</span></li>
        </ul>
      </div>
    </article>

    <article class="depot">
      <svg class="depot-photo" role="img" aria-label="Ottawa parliament hill at dusk"><defs><linearGradient id="g9" x1="0" y1="0" x2="0" y2="1"><stop offset="0" stop-color="#4a5aa0"/><stop offset=".5" stop-color="#8a6a8a"/><stop offset="1" stop-color="#3a4a4a"/></linearGradient></defs><rect width="429" height="194" fill="url(#g9)"/></svg>
      <h2 class="city">Ottawa</h2>
      <div class="depot-info">
        <ul>
          <li><svg><use href="#i-pin"/></svg><span>Ottawa, Ontario,<br>Canada</span></li>
          <li><svg><use href="#i-clock"/></svg><span>Monday - Friday<br>( 9am - 5pm )</span></li>
        </ul>
        <ul>
          <li><svg><use href="#i-phone"/></svg><span>1.877.5.GREENS (Toll Free)</span></li>
          <li><svg><use href="#i-mail"/></svg><span>ottawa@umk.ca</span></li>
          <li class="map-link"><svg><use href="#i-map"/></svg><span>Map to Warehouse</span></li>
        </ul>
      </div>
    </article>

    <article class="depot">
      <svg class="depot-photo" role="img" aria-label="Barrie town centre by day"><defs><linearGradient id="g10" x1="0" y1="0" x2="0" y2="1"><stop offset="0" stop-color="#9ab8d8"/><stop offset=".5" stop-color="#a49a88"/><stop offset="1" stop-color="#6a7260"/></linearGradient></defs><rect width="429" height="194" fill="url(#g10)"/></svg>
      <h2 class="city">Barrie</h2>
      <div class="depot-info">
        <ul>
          <li><svg><use href="#i-pin"/></svg><span>Barrie, Ontario,<br>Canada</span></li>
          <li><svg><use href="#i-clock"/></svg><span>Monday - Friday<br>( 9am - 5pm )</span></li>
        </ul>
        <ul>
          <li><svg><use href="#i-phone"/></svg><span>1.877.5.GREENS (Toll Free)</span></li>
          <li><svg><use href="#i-mail"/></svg><span>barrie@umk.ca</span></li>
          <li class="map-link"><svg><use href="#i-map"/></svg><span>Map to Warehouse</span></li>
        </ul>
      </div>
    </article>

    <article class="depot">
      <svg class="depot-photo" role="img" aria-label="Dartmouth harbour bridge lit at night"><defs><linearGradient id="g11" x1="0" y1="0" x2="0" y2="1"><stop offset="0" stop-color="#1a1a1e"/><stop offset=".5" stop-color="#3a4a2a"/><stop offset="1" stop-color="#6a4a22"/></linearGradient></defs><rect width="429" height="194" fill="url(#g11)"/></svg>
      <h2 class="city">Dartmouth</h2>
      <div class="depot-info">
        <ul>
          <li><svg><use href="#i-pin"/></svg><span>Dartmouth,<br>Nova Scotia, Canada</span></li>
          <li><svg><use href="#i-clock"/></svg><span>Monday - Friday<br>( 9am - 5pm )</span></li>
        </ul>
        <ul>
          <li><svg><use href="#i-phone"/></svg><span>1.877.5.GREENS (Toll Free)</span></li>
          <li><svg><use href="#i-mail"/></svg><span>dartmouth@umk.ca</span></li>
          <li class="map-link"><svg><use href="#i-map"/></svg><span>Map to Warehouse</span></li>
        </ul>
      </div>
    </article>
  </div>
</main>

<footer class="site-footer">
  <div class="newsletter">
    <svg viewBox="0 0 34 28" aria-hidden="true"><path d="M0 12 34 0 26 28 16 19 28 5 12 17z"/></svg>
    <span class="newsletter-label">Subscribe Our Newsletter</span>
    <span class="newsletter-input">Enter Your Email Address</span>
    <span class="newsletter-button">Subscribe</span>
  </div>
  <div class="footer-rule"></div>

  <section class="footer-col quick-links">
    <h2>Quick Links</h2>
    <div class="lists">
      <ul><li>About Us</li><li>Drop off Items</li><li>Depots</li><li>Jobs</li><li>Volunteer</li></ul>
      <ul><li>Pictures and Videos</li><li>Links</li><li>Memberships</li><li>News</li><li>Contact us</li></ul>
    </div>
  </section>

  <section class="footer-col payments">
    <h2>Payments Method</h2>
    <ul class="payment-cards">
      <li class="card">Corvia</li><li class="card">Payloop</li>
      <li class="card">Tallycard</li><li class="card">Nexpay</li>
      <li class="card">Atlas</li>
    </ul>
  </section>

  <section class="footer-col connect">
    <h2>Stay Connect</h2>
    <ul class="social" aria-label="Social networks">
      <li></li><li></li><li></li><li></li><li></li>
    </ul>
    <div class="contact-info">
      <h3>Contact Information</h3>
      <p class="city-line">Calgary</p>
      <p>1300 52nd Avenue SE<br>Calgary, Alberta, Canada</p>
      <p class="big-phone">403.555.0148</p>
    </div>
  </section>
  <div class="footer-divider"></div>
</footer>

<div class="legal">
  <p>Copyright © 2013 UMK.CA. All Rights Reserved. Site by UMK - Unified Material Keepers</p>
  <ul class="regions" aria-label="Provincial flags">
    <li style="background:#c8282c"></li><li style="background:#2a4a9a"></li><li style="background:#1e3a8a"></li><li style="background:#b8262a"></li><li style="background:#2a5aa8"></li><li style="background:#1e4aa0"></li>
  </ul>
</div>
</body>
</html>
```